Luxury Eco accommodation needs new website

Luxury lodge accommodation on exclusive private property in Flinders Ranges South Australia.
Brand new venture needs new site.
Focus on small group accommodation on exclusive property with outdoor experiences. Mountain biking , bush walking, outdoor dining.
We currently have a website but are having trouble making it our own. Needs to be "polished" by a professional.
Can you help?

www.larkhollowretreat.com.au

Target Market(s)

High income travellers, luxury accommodation

Industry/Entity Type

Accommodation

```html
<!DOCTYPE html>
<html lang="en">
<head>
<meta charset="utf-8">
<title>Lark Hollow Retreat</title>
<link href="https://fonts.googleapis.com/css2?family=Glegoo&family=Petit+Formal+Script&display=swap" rel="stylesheet">
<style>
  :root {
    --page-bg: #ffffff;
    --header-band: #f2f5f9;
    --header-rule: #dfe3e8;
    --ink: #3a3a3a;
    --ink-soft: #555555;
    --rule: #bdbdbd;
    --brown: #8a4f1c;
    --brown-dark: #6e3b12;
    --sign-wood: #d9b879;
    --sign-edge: #b8925a;
    --sign-ink: #2e2416;
    --active-tab: #fbefe6;
    --social: #e08a3a;
  }
  * { margin: 0; padding: 0; box-sizing: border-box; }
  html, body { width: 1200px; height: 878px; overflow: hidden; background: var(--page-bg); }
  body { position: relative; font-family: "Glegoo", Georgia, serif; color: var(--ink); }

  .site-header { position: absolute; left: 0; top: 0; width: 1200px; height: 112px; }
  .site-header__band {
    position: absolute; left: 0; top: 33px; width: 100%; height: 79px;
    background: var(--header-band); border-bottom: 1px solid var(--header-rule);
  }
  .brand {
    position: absolute; left: 158px; top: 0; width: 147px; height: 112px;
    background: #fff; border: 1px solid var(--header-rule); border-top: none;
    box-shadow: 0 1px 3px rgba(0,0,0,.08);
    display: flex; flex-direction: column; align-items: center; justify-content: center; gap: 8px;
  }
  .brand__square { width: 26px; height: 26px; background: var(--brown); }
  .brand__name { font-size: 15px; letter-spacing: 1.5px; color: var(--ink-soft); text-align: center; line-height: 1.2; }

  .main-nav { position: absolute; top: 35px; left: 392px; display: flex; }
  .main-nav a {
    display: block; height: 44px; line-height: 46px; padding: 0 21px;
    font-size: 16px; color: var(--ink); text-decoration: none; letter-spacing: .2px;
  }
  .main-nav a.is-active {
    background: var(--active-tab); border-top: 2px solid #e8dcd2; border-radius: 3px 3px 0 0;
    box-shadow: 0 1px 3px rgba(0,0,0,.05);
  }

  .hero { position: absolute; left: 0; top: 112px; width: 1200px; height: 535px; overflow: hidden; }
  .hero__photo {
    position: absolute; inset: 0;
    background: linear-gradient(180deg, #eef2f5 0%, #f1e6e2 28%, #c98a6a 45%, #8e5a46 58%, #5c3a30 70%, #8a5a44 82%, #a56e52 100%);
  }
  .hero__quote {
    position: absolute; left: 152px; top: 96px;
    font-family: "Petit Formal Script", cursive; font-size: 19px; line-height: 32px; color: #2d2b2b;
  }
  .booking-sign {
    position: absolute; left: 876px; top: 320px; width: 266px; height: 124px;
    background: var(--sign-wood); border: 2px solid var(--sign-edge); border-radius: 4px;
    transform: rotate(-2.5deg); box-shadow: 2px 3px 6px rgba(0,0,0,.35);
    display: flex; flex-direction: column; align-items: center; justify-content: center; gap: 6px;
    color: var(--sign-ink); font-size: 14px;
  }
  .booking-sign__title { letter-spacing: .5px; font-size: 14px; }

  .slider-dots {
    position: absolute; left: 544px; top: 632px; width: 107px; height: 30px;
    background: #fff; border-radius: 15px; box-shadow: 0 2px 5px rgba(0,0,0,.2);
    display: flex; align-items: center; justify-content: center; gap: 9px;
  }
  .slider-dots span { width: 13px; height: 13px; border-radius: 50%; border: 1px solid #b9b9b9; background: #f4f4f4; }
  .slider-dots span.is-current { background: #d5d5d5; }

  .welcome { position: absolute; left: 114px; top: 684px; width: 959px; text-align: center; }
  .welcome__title { display: flex; align-items: center; gap: 14px; font-weight: normal; font-size: 19px; color: var(--ink); letter-spacing: .3px; }
  .welcome__title::before, .welcome__title::after { content: ""; flex: 1; height: 1px; background: var(--rule); }
  .welcome__text { margin-top: 6px; font-size: 15px; line-height: 21px; color: var(--ink); letter-spacing: .2px; }
  .btn-more {
    display: inline-block; margin-top: 12px; padding: 0 11px; height: 27px; line-height: 29px;
    background: var(--brown); color: #fff; font-size: 15px; text-decoration: none;
    border-bottom: 2px solid var(--brown-dark);
  }

  .site-footer { position: absolute; left: 0; top: 838px; width: 1200px; height: 28px; font-size: 13px; color: var(--ink-soft); }
  .site-footer__copy { position: absolute; left: 491px; top: 6px; }
  .site-footer__social { position: absolute; left: 788px; top: 0; display: flex; align-items: center; gap: 6px; }
  .site-footer__social span { margin-right: 2px; }
  .social-tile { width: 24px; height: 24px; background: var(--social); border-radius: 4px; box-shadow: 0 1px 2px rgba(0,0,0,.3); }
</style>
</head>
<body>
  <header class="site-header">
    <div class="site-header__band"></div>
    <div class="brand">
      <div class="brand__square"></div>
      <div class="brand__name">LARK HOLLOW</div>
    </div>
    <nav class="main-nav">
      <a href="#" class="is-active">LUXURY LODGE</a>
      <a href="#">OTHER STAYS</a>
      <a href="#">EXPERIENCES</a>
      <a href="#">GALLERY</a>
      <a href="#">CONTACT US</a>
    </nav>
  </header>

  <section class="hero">
    <div class="hero__photo" role="img" aria-label="Photo of guests looking out over sunlit rugged mountain ranges above a pine-covered valley"></div>
    <blockquote class="hero__quote">“ The bones of the earth laid bare.”<br>– Sir Edmund Varley</blockquote>
    <div class="booking-sign">
      <div class="booking-sign__title">FOR BOOKINGS &amp; INFORMATION:</div>
      <div>(08) 8555 0142</div>
      <div>larkhollow.retreat@mail.com</div>
    </div>
  </section>

  <div class="slider-dots"><span class="is-current"></span><span></span><span></span><span></span></div>

  <main class="welcome">
    <h1 class="welcome__title">Welcome to our site</h1>
    <p class="welcome__text">Lark Hollow Lodge is nestled in the heart of SA’s magnificent Flinders Ranges. It is located on Lark Hollow Retreat, 480 kms north of Adelaide and stretches along the northern boundary of the great Flinders Ranges National Park. The Lodge is tucked into a ridge top near the homestead and overlooks a valley of river red gums and native pines.</p>
    <a href="#" class="btn-more">More</a>
  </main>

  <footer class="site-footer">
    <div class="site-footer__copy">Copyright@2013, Lark Hollow Retreat</div>
    <div class="site-footer__social"><span>Follow Us :</span><div class="social-tile"></div><div class="social-tile"></div></div>
  </footer>
</body>
</html>
```